Home page web design for "Tales from Thee"

We need a home page web design for a start up company that will write memoirs for seniors.
The completed project will need to include PSD files...NO HTML or CSS necessary.
Attached is a brief outline concept that may give you some ideas...but you are the creative professionals, so please feel free to add your ideas. We will also attach some files that show you our logo, brochures, and photos that could be used to give you ideas of our focus.
There will need to be access to the other pages on the home page to include: 'About Us'; 'How We Can Help'; 'Community Sessions'; 'Senior Consulting ' and 'Contact Us'.
Updates

Target Market(s)

Seniors and Baby Boomers

Industry/Entity Type

It Company

Number of Pages Required

1 page

Colors
f9ba93
fbca95
faa54b
faf289
f37123

Requirements
Must have
• Script easy on senior eyes.
• Initial contact number would be 844-4LANTERN
Nice to have
• While the color pallet is non-specific we prefer the warm colors.
• salmon, peach.......
• NOT so much the orange of Halloween:)
• However, please utilize your creativity and put in colors you feel will draw best with your design.

```html
<!DOCTYPE html>
<html lang="en">
<head>
<meta charset="utf-8">
<title>Tales from Thee — Home</title>
<link href="https://fonts.googleapis.com/css2?family=Source+Sans+3:ital,wght@0,400;0,600;1,400;1,600&family=Italianno&display=swap" rel="stylesheet">
<style>
:root{
  --orange:#f37123;
  --salmon:#f9a48a;
  --peach:#fbca95;
  --cream:#fde6cc;
  --ink:#3a3a3a;
  --script:#2a1a14;
  --white:#ffffff;
}
*{box-sizing:border-box;margin:0;padding:0}
html,body{width:1200px;height:1000px;overflow:hidden}
body{position:relative;background:var(--peach);font-family:"Source Sans 3",sans-serif;color:var(--ink)}
.site-header{position:absolute;left:0;top:0;width:1200px;height:87px;background:var(--white);border-top:3px solid var(--orange)}
.nav-link{position:absolute;top:36px;font-size:14px;font-style:italic;font-weight:600;color:#555;text-transform:uppercase;text-decoration:none;letter-spacing:-.2px}
.nav-link.active{left:100px;top:27px;width:86px;height:36px;line-height:36px;text-align:center;background:var(--orange);color:var(--white);font-size:13px}
.brand-mark{position:absolute;left:478px;top:8px;width:148px;height:72px;border:1px solid #e6d6b8;border-radius:50%;display:flex;align-items:center;justify-content:center;font-family:"Italianno",cursive;font-size:28px;color:#7a5a2a}
.hero{position:absolute;left:0;top:87px;width:1200px;height:497px;background:radial-gradient(ellipse at center,#fcb8a0 0%,var(--salmon) 70%)}
.hero-photo{position:absolute;border-radius:50%;border:3px solid #f5d37a;box-shadow:0 0 14px rgba(255,240,220,.8)}
.photo-left{left:27px;top:20px;width:304px;height:420px;background:linear-gradient(180deg,#c56a26 0%,#7a2a10 45%,#1a0806 80%)}
.photo-right{left:880px;top:18px;width:286px;height:416px;background:linear-gradient(160deg,#6a4a30 0%,#3a2618 55%,#b8a898 100%)}
.hero-url{position:absolute;left:0;width:1200px;top:8px;text-align:center;font-family:"Italianno",cursive;font-size:56px;color:var(--script);padding-left:4px}
.hero-phones{position:absolute;left:330px;top:64px;font-family:"Italianno",cursive;font-size:40px;color:var(--script);display:flex;gap:22px;align-items:center}
.hero-phones span{display:flex;align-items:center;gap:10px}
.hero-name{position:absolute;left:355px;top:130px;width:505px;height:240px;border:2px solid #c87a30;border-radius:50%;display:flex;align-items:center;justify-content:center;font-family:"Italianno",cursive;font-size:80px;color:#8a3a10}
.hero-rule{position:absolute;left:362px;top:416px;width:468px;height:2px;background:linear-gradient(90deg,transparent,#f4e0d8,transparent)}
.tag-left{position:absolute;left:14px;top:440px;font-family:"Italianno",cursive;font-size:40px;color:var(--script)}
.tag-right{position:absolute;left:836px;top:444px;width:350px;text-align:center;font-family:"Italianno",cursive;font-size:34px;line-height:21px;color:var(--script)}
.section-title{position:absolute;left:106px;top:600px;font-size:22px;font-style:italic;font-weight:600;color:var(--orange);padding-bottom:2px;border-bottom:1px solid var(--orange);width:184px}
.packages{position:absolute;left:0;top:650px}
.package{position:absolute;width:214px;text-align:center;color:var(--ink)}
.package h3{font-size:20px;font-style:italic;font-weight:600;color:var(--orange);margin-bottom:4px}
.package p{font-size:12.5px;line-height:18px}
.package .size{font-size:24px;font-style:italic;font-weight:600;color:var(--orange);margin:8px 0 10px}
.group-note{position:absolute;left:0;top:904px;width:1222px;text-align:center;font-size:14.5px;line-height:23px;color:#333}
.next-title{position:absolute;left:106px;top:986px;font-size:22px;font-style:italic;font-weight:600;color:var(--orange)}
</style>
</head>
<body>
<header class="site-header">
  <a class="nav-link active" href="#">Home Page</a>
  <a class="nav-link" style="left:218px" href="#">About Us</a>
  <a class="nav-link" style="left:318px" href="#">How We Can Help</a>
  <div class="brand-mark">Tales from Thee</div>
  <a class="nav-link" style="left:650px" href="#">Community Services</a>
  <a class="nav-link" style="left:815px" href="#">Senior Consulting Services</a>
  <a class="nav-link" style="left:1028px" href="#">Contact Us</a>
</header>

<section class="hero">
  <div class="hero-photo photo-left" role="img" aria-label="Photo of an older couple walking along a beach at sunset"></div>
  <div class="hero-photo photo-right" role="img" aria-label="Photo of an elderly woman writing at a wooden desk by lamplight"></div>
  <div class="hero-url">www.talesfromthee.com</div>
  <div class="hero-phones">
    <span><svg width="24" height="20" viewBox="0 0 24 20"><ellipse cx="12" cy="8" rx="11" ry="7.5" fill="#2a1a14"/><path d="M6 13 L4 19 L11 14Z" fill="#2a1a14"/></svg>717-555-0142</span>
    <span><svg width="24" height="20" viewBox="0 0 24 20"><ellipse cx="12" cy="8" rx="11" ry="7.5" fill="#2a1a14"/><path d="M6 13 L4 19 L11 14Z" fill="#2a1a14"/></svg>844-4LANTERN</span>
  </div>
  <div class="hero-name">Tales from Thee</div>
  <div class="hero-rule"></div>
  <div class="tag-left">When a genealogy doesn't say enough...</div>
  <div class="tag-right">Every life legacy is a gift to be treasured by the next generation</div>
</section>

<h2 class="section-title">PACKAGE DETAILS</h2>

<svg class="packages" width="1200" height="250" viewBox="0 0 1200 250" aria-hidden="true">
  <defs>
    <radialGradient id="disc" cx="50%" cy="45%" r="55%">
      <stop offset="0" stop-color="#fde6cc"/><stop offset=".85" stop-color="#fbe0c2"/><stop offset="1" stop-color="#c8b8a8"/>
    </radialGradient>
    <radialGradient id="shadow" cx="50%" cy="50%" r="50%">
      <stop offset="0" stop-color="#555" stop-opacity=".6"/><stop offset="1" stop-color="#555" stop-opacity="0"/>
    </radialGradient>
  </defs>
  <ellipse cx="448" cy="114" rx="110" ry="62" fill="#f37123"/>
  <ellipse cx="806" cy="114" rx="110" ry="62" fill="#f37123"/>
  <path d="M400 108 Q440 132 468 112 L462 96 L484 110 L470 138 L468 124 Q430 148 400 108Z" fill="#f5a37a"/>
  <path d="M756 108 Q796 132 824 112 L818 96 L840 110 L826 138 L824 124 Q786 148 756 108Z" fill="#f5a37a"/>
  <g>
    <ellipse cx="262" cy="230" rx="70" ry="8" fill="url(#shadow)"/>
    <ellipse cx="616" cy="230" rx="70" ry="8" fill="url(#shadow)"/>
    <ellipse cx="976" cy="230" rx="70" ry="8" fill="url(#shadow)"/>
    <circle cx="268" cy="118" r="108" fill="url(#disc)" stroke="#f37123" stroke-width="3"/>
    <circle cx="620" cy="118" r="108" fill="url(#disc)" stroke="#f37123" stroke-width="3"/>
    <circle cx="978" cy="118" r="108" fill="url(#disc)" stroke="#f37123" stroke-width="3"/>
  </g>
</svg>

<div class="package" style="left:164px;top:696px">
  <h3>PACKAGE I</h3>
  <p>Standard portrait book with up to 120 pages or 18,000 words</p>
  <div class="size">8 x 10</div>
  <p>includes photos and<br>text throughout</p>
</div>
<div class="package" style="left:509px;top:696px">
  <h3>PACKAGE II</h3>
  <p>Standard Trade book up to 250 pages or 100,000 words</p>
  <div class="size">6 x 9</div>
  <p>Few photos mainly text</p>
</div>
<div class="package" style="left:868px;top:696px">
  <h3>PACKAGE III</h3>
  <p>Standard portrait book with up to 120 to 200 pages or 18k to 54k words</p>
  <div class="size">8 x 10</div>
  <p>includes photos and<br>text throughout</p>
</div>

<p class="group-note">we offer 12 weekly&nbsp; packages for groups of 10 or more. if you and tour retirement&nbsp; or community group<br>would like to begin your memories together, we can bring our expertise&nbsp; to you!</p>

<h2 class="next-title">WHAT IS TALES FROM THEE</h2>
</body>
</html>
```